App Design - Job Lantern Quokka

We require an App Design for our new App called 'Lantern Quokka'. This app is essentially an assistant to help Users prepare for job interviews, to help them get hired. <br/><br/>Users who download the App can view common Questions and Answers, save their favourite responses and also view common Interview Tips. <br/><br/>The vision for our App is for Users who are preparing for an interview (1 week before, 1 day before, even 1 hour before), are able to download, view and educate themselves on common questions and responses, and then be confident to land the job. <br/><br/>Our team has developed wireframes to help highlight what each screen should do and include. Please see attached document, which also highlights key requirements for the experience. Feel free to add/remove/edit what you see on these wireframes. Our preference is that you use Adobe XD please.<br/><br/>In terms of design guidelines, we want the experience to be simple, intuitive and 'memorable' to help Users to remember the questions/responses when they are in the interview. <br/><br/>The final design should communicate 'neat and clean professionalism'; we like the design of: marlo vane com au<br/><br/>Thank you for reading! Good luck !

Target Market(s)

Professional job seekers

Font styles to use
Sans Serif

Colors

Designer to choose colors to be used in the design.

Requirements
Must have
• Please see my PlanHive_UX file that I have uploaded
Nice to have
• Could you also please include some ideas on how we can incorporate Advertising into the app screens

```html
<!DOCTYPE html>
<html lang="en">
<head>
<meta charset="utf-8">
<title>Lantern Quokka – App Screens</title>
<link rel="stylesheet" href="https://fonts.googleapis.com/css2?family=Rubik:wght@400;500;600&display=swap">
<style>
:root{
  --indigo:#4d5ffd;
  --teal:#00c3a5;
  --coral:#fd5a5e;
  --amber:#ffc400;
  --surface:#f0f1f6;
  --card:#ffffff;
  --ink:#2b2d3c;
  --muted:#55586a;
  --backdrop:#ffffff;
}
*{box-sizing:border-box;margin:0;padding:0}
html,body{width:1200px;height:2339px;overflow:hidden;background:var(--backdrop)}
body{position:relative;font-family:"Rubik",sans-serif;color:var(--ink)}
.screen{position:absolute;width:290px;height:628px;border-radius:34px;overflow:hidden;background:var(--surface);box-shadow:0 18px 36px rgba(77,95,253,.16)}
.c1{left:99px}.c2{left:454px}.c3{left:811px}
.r1{top:121px}.r2{top:840px}.r3{top:1561px}
.abs{position:absolute}

/* app bar */
.app-bar{position:absolute;left:0;top:0;width:100%;height:78px;background:var(--indigo);color:#fff}
.app-bar .back{position:absolute;left:18px;top:42px;width:12px;height:18px}
.app-bar .brand{position:absolute;left:0;right:0;top:40px;text-align:center;font-size:17px;font-weight:600}
.title-bar{position:absolute;left:0;top:78px;width:100%;height:50px;background:#fff;border-bottom:1px solid #e2e3ea;display:flex;align-items:center;justify-content:center;gap:12px;font-size:15px;font-weight:500}
.title-bar.left{justify-content:flex-start;padding-left:20px}
.badge{width:28px;height:28px;border-radius:50%;display:flex;align-items:center;justify-content:center;box-shadow:0 3px 6px rgba(0,0,0,.15);flex:none}
.badge svg{width:14px;height:14px}
.teal{background:var(--teal)}.coral{background:var(--coral)}.amber{background:var(--amber)}

.prompt{position:absolute;left:0;right:0;text-align:center;font-size:11.5px;color:var(--muted)}
.cat-btn{position:absolute;left:18px;width:254px;height:50px;border-radius:5px;background:var(--indigo);color:#fff;font-size:14px;font-weight:500;display:flex;align-items:center;justify-content:center;box-shadow:0 6px 10px rgba(77,95,253,.3)}
.see-all{position:absolute;left:70px;width:150px;height:37px;border:1.5px solid var(--indigo);border-radius:6px;color:var(--indigo);font-size:13px;font-weight:500;display:flex;align-items:center;justify-content:center;background:#fff}

.band{position:absolute;left:0;width:100%;top:128px;color:#fff;font-size:13.5px;font-weight:500;text-align:center}
.band.teal{height:33px;line-height:33px}

.q-card{position:absolute;left:13px;width:264px;background:var(--card);border-radius:5px;box-shadow:0 3px 8px rgba(0,0,0,.06);display:flex;align-items:center;gap:14px;padding:8px 12px 8px 8px;font-size:11px;line-height:1.35;color:var(--muted)}
.num{width:22px;height:22px;border-radius:4px;color:#fff;font-size:11.5px;font-weight:600;display:flex;align-items:center;justify-content:center;flex:none;box-shadow:0 3px 5px rgba(0,0,0,.15)}
.num.teal{background:var(--teal)}.num.amber{background:var(--amber)}.num.coral{background:var(--coral)}

.dots{position:absolute;left:0;right:0;display:flex;justify-content:center;gap:6px}
.dots i{width:5px;height:5px;border-radius:50%;background:rgba(255,255,255,.55)}
.dots i:first-child{background:#fff}
.carousel-edge{position:absolute;width:6px;height:72px;background:#fff;border-radius:4px}

.resp{position:absolute;left:11px;width:268px;height:72px;background:#fff;border-radius:5px;box-shadow:0 3px 8px rgba(0,0,0,.07);padding:24px 14px 0 12px;font-size:11px;line-height:1.35;color:var(--muted)}
.resp .tag{position:absolute;left:0;top:4px;background:var(--teal);color:#fff;font-size:9px;font-weight:500;padding:2px 7px;border-radius:0 4px 4px 0}
.resp .star{position:absolute;right:6px;top:5px;width:16px;height:16px}
.resp p{display:-webkit-box;-webkit-line-clamp:3;-webkit-box-orient:vertical;overflow:hidden}

.fav{position:absolute;left:12px;width:266px;background:#fff;border-radius:5px;box-shadow:0 3px 8px rgba(0,0,0,.07);padding:10px 22px 10px 40px;font-size:11px;line-height:1.35;color:var(--muted)}
.fav .num{position:absolute;left:8px;top:10px}
.fav h4{font-size:11.5px;font-weight:500;color:var(--ink);margin-bottom:8px}
.fav .close{position:absolute;right:8px;top:8px;width:14px;height:14px;border-radius:50%;background:#fde3e4}

.tip{position:absolute;left:13px;width:264px;height:50px;background:#fff;border-radius:5px;box-shadow:0 3px 8px rgba(0,0,0,.06);display:flex;align-items:center;gap:14px;padding:0 12px 0 8px;font-size:11px;line-height:1.35;color:var(--muted)}
</style>
</head>
<body>

<!-- 1 Splash -->
<section class="screen c1 r1" style="background:var(--indigo);color:#fff">
  <div class="abs" style="left:0;right:0;top:272px;text-align:center;font-size:24px;font-weight:600">Lantern Quokka</div>
  <p class="abs" style="left:34px;right:34px;top:318px;text-align:center;font-size:12.5px;line-height:1.4;font-weight:500">Your guide to the most common interview questions, and the best responses to help you get hired</p>
</section>

<!-- 2 Home -->
<section class="screen c2 r1" style="background:var(--indigo)">
  <div class="abs" style="left:0;top:0;width:290px;height:190px;background:var(--surface)"></div>
  <div class="abs" style="left:22px;top:64px;font-size:17px;color:#8a8d9c">Welcome to</div>
  <div class="abs" style="left:22px;top:88px;font-size:21px;font-weight:600;color:var(--indigo)">Lantern Quokka</div>
  <div class="abs" role="img" aria-label="Illustration of two people at a table during a job interview" style="left:40px;top:132px;width:220px;height:158px;border-radius:12px;background:linear-gradient(160deg,#dfe1f3 0%,#8e98fb 55%,#3f4ed8 100%)"></div>
  <div class="abs" style="left:22px;top:318px;width:115px;height:127px;background:#fff;border-radius:6px;text-align:center;font-size:11.5px;font-weight:500;line-height:1.3;padding-top:20px">
    <div class="badge teal" style="width:52px;height:52px;margin:0 auto 10px"><svg viewBox="0 0 16 16"><circle cx="8" cy="8" r="7" fill="#fff"/><text x="8" y="11.5" font-size="10" text-anchor="middle" fill="#00c3a5" font-family="Rubik,sans-serif" font-weight="600">?</text></svg></div>
    View Questions<br>&amp; Responses
  </div>
  <div class="abs" style="left:158px;top:318px;width:115px;height:127px;background:#fff;border-radius:6px;text-align:center;font-size:11.5px;font-weight:500;line-height:1.3;padding-top:20px">
    <div class="badge coral" style="width:52px;height:52px;margin:0 auto 10px"><svg viewBox="0 0 16 16"><path d="M8 1.5l1.9 4.2 4.6.4-3.5 3 1.1 4.5L8 11.3 3.9 13.6 5 9.1 1.5 6.1l4.6-.4z" fill="#fff"/></svg></div>
    My Questions<br>Portfolio
  </div>
  <div class="abs" style="left:22px;top:468px;width:115px;height:127px;background:#fff;border-radius:6px;text-align:center;font-size:11.5px;font-weight:500;line-height:1.3;padding-top:20px">
    <div class="badge amber" style="width:52px;height:52px;margin:0 auto 14px"><svg viewBox="0 0 16 16"><path d="M8 1.5a4.5 4.5 0 0 0-2.6 8.2V12h5.2V9.7A4.5 4.5 0 0 0 8 1.5z" fill="#fff"/><rect x="5.8" y="12.8" width="4.4" height="1.6" rx=".8" fill="#fff"/></svg></div>
    Interview Tips
  </div>
</section>

<!-- 3 Question categories -->
<section class="screen c3 r1">
  <header class="app-bar"><svg class="back" viewBox="0 0 12 18"><path d="M10 2L3 9l7 7" stroke="#fff" stroke-width="2.2" fill="none" stroke-linecap="round"/></svg><div class="brand">Lantern Quokka</div></header>
  <div class="title-bar"><span class="badge teal"><svg viewBox="0 0 16 16"><circle cx="8" cy="8" r="7" fill="#fff"/><text x="8" y="11.5" font-size="10" text-anchor="middle" fill="#00c3a5" font-family="Rubik,sans-serif">?</text></svg></span>View Questions&amp; Responses</div>
  <p class="prompt" style="top:166px">Select your question category</p>
  <div class="cat-btn" style="top:208px">Behavioural</div>
  <div class="cat-btn" style="top:284px">Situational</div>
  <div class="cat-btn" style="top:361px">Motivational</div>
  <div class="cat-btn" style="top:436px">Technical</div>
  <div class="see-all" style="top:515px">See all</div>
</section>

<!-- 4 Behavioural list -->
<section class="screen c1 r2">
  <header class="app-bar"><svg class="back" viewBox="0 0 12 18"><path d="M10 2L3 9l7 7" stroke="#fff" stroke-width="2.2" fill="none" stroke-linecap="round"/></svg><div class="brand">Lantern Quokka</div></header>
  <div class="title-bar left"><span class="badge teal"><svg viewBox="0 0 16 16"><circle cx="8" cy="8" r="7" fill="#fff"/><text x="8" y="11.5" font-size="10" text-anchor="middle" fill="#00c3a5" font-family="Rubik,sans-serif">?</text></svg></span>View Questions&amp; Responses</div>
  <div class="band teal">Behavioural</div>
  <div class="q-card" style="top:175px;height:72px"><span class="num teal">1</span>Lorem ipsum dolor sit amet, consectetuer adipiscing elit, sed diam nonummy nibh euismod tincidunt ut laoreet dolore magna aliquam erat volutpat.</div>
  <div class="q-card" style="top:265px;height:72px"><span class="num teal">2</span>Lorem ipsum dolor sit amet, consectetuer adipiscing elit, sed diam nonummy nibh euismod tincidunt ut laoreet dolore magna aliquam erat volutpat.</div>
  <div class="q-card" style="top:355px;height:72px"><span class="num teal">3</span>Lorem ipsum dolor sit amet, consectetuer adipiscing elit, sed diam nonummy nibh euismod</div>
  <div class="q-card" style="top:445px;height:72px"><span class="num teal">4</span>Lorem ipsum dolor sit amet, consectetuer adipiscing elit</div>
  <div class="q-card" style="top:535px;height:72px"><span class="num teal">5</span>Lorem ipsum dolor sit amet, consectetuer adipiscing elit, sed diam nonummy nibh euismod tincidunt</div>
</section>

<!-- 5 Question detail with responses -->
<section class="screen c2 r2" style="background:#dfe1ee">
  <header class="app-bar"><svg class="back" viewBox="0 0 12 18"><path d="M10 2L3 9l7 7" stroke="#fff" stroke-width="2.2" fill="none" stroke-linecap="round"/></svg><div class="brand">Lantern Quokka</div></header>
  <div class="title-bar left"><span class="badge teal"><svg viewBox="0 0 16 16"><circle cx="8" cy="8" r="7" fill="#fff"/><text x="8" y="11.5" font-size="10" text-anchor="middle" fill="#00c3a5" font-family="Rubik,sans-serif">?</text></svg></span>View Questions&amp; Responses</div>
  <div class="band teal" style="height:150px;line-height:33px">Behavioural</div>
  <div class="carousel-edge" style="left:0;top:168px"></div>
  <div class="carousel-edge" style="right:0;top:168px"></div>
  <div class="q-card" style="top:168px;height:72px"><span class="num teal">1</span>Lorem ipsum dolor sit amet, consectetuer adipiscing elit, sed diam nonummy nibh euismod tincidunt ut laoreet dolore magna aliquam erat volutpat.</div>
  <div class="dots" style="top:256px"><i></i><i></i><i></i><i></i><i></i><i></i><i></i><i></i></div>
  <div class="resp" style="top:285px"><span class="tag">Respond 1</span><svg class="star" viewBox="0 0 16 16"><path d="M8 1.5l1.9 4.2 4.6.4-3.5 3 1.1 4.5L8 11.3 3.9 13.6 5 9.1 1.5 6.1l4.6-.4z" fill="var(--coral)"/></svg><p>Lorem ipsum dolor sit amet, consectetuer adipiscing elit, sed diam nonummy nibh euismod tincidunt ut laoreet dolore magna aliquam</p></div>
  <div class="resp" style="top:372px"><span class="tag">Respond 2</span><svg class="star" viewBox="0 0 16 16"><path d="M8 1.5l1.9 4.2 4.6.4-3.5 3 1.1 4.5L8 11.3 3.9 13.6 5 9.1 1.5 6.1l4.6-.4z" fill="#e6e7ee"/></svg><p>Lorem ipsum dolor sit amet, consectetuer adipiscing elit, sed diam nonummy nibh euismod tincidunt ut laoreet dolore magna aliquam</p></div>
  <div class="resp" style="top:459px"><span class="tag">Respond 3</span><svg class="star" viewBox="0 0 16 16"><path d="M8 1.5l1.9 4.2 4.6.4-3.5 3 1.1 4.5L8 11.3 3.9 13.6 5 9.1 1.5 6.1l4.6-.4z" fill="var(--coral)"/></svg><p>Lorem ipsum dolor sit amet, consectetuer adipiscing elit, sed diam nonummy nibh euismod tincidunt ut laoreet dolore magna aliquam</p></div>
  <div class="resp" style="top:546px"><span class="tag">Respond 4</span><svg class="star" viewBox="0 0 16 16"><path d="M8 1.5l1.9 4.2 4.6.4-3.5 3 1.1 4.5L8 11.3 3.9 13.6 5 9.1 1.5 6.1l4.6-.4z" fill="#e6e7ee"/></svg><p>Lorem ipsum dolor sit amet, consectetuer adipiscing elit, sed diam nonummy nibh euismod tincidunt ut laoreet dolore magna aliquam</p></div>
</section>

<!-- 6 Portfolio -->
<section class="screen c3 r2">
  <header class="app-bar"><svg class="back" viewBox="0 0 12 18"><path d="M10 2L3 9l7 7" stroke="#fff" stroke-width="2.2" fill="none" stroke-linecap="round"/></svg><div class="brand">Lantern Quokka</div></header>
  <div class="title-bar left" style="padding-left:30px"><span class="badge coral"><svg viewBox="0 0 16 16"><path d="M8 1.5l1.9 4.2 4.6.4-3.5 3 1.1 4.5L8 11.3 3.9 13.6 5 9.1 1.5 6.1l4.6-.4z" fill="#fff"/></svg></span>My Question Portfolio</div>
  <p class="prompt" style="top:146px;line-height:1.35">These are yor saved answers that you favourited.<br>We place them here to help you prepare.</p>
  <div class="fav" style="top:196px;height:107px"><span class="num coral">4</span><span class="close"></span><h4>What are your greatest strengths?</h4>Lorem ipsum dolor sit amet, consectetuer adipiscing elit, sed diam nonummy nibh euismod tincidunt ut laoreet dolore magna aliquam erat</div>
  <div class="fav" style="top:319px;height:108px"><span class="num coral">20</span><span class="close"></span><h4>Lorem ipsum dolor sit amet?</h4>Lorem ipsum dolor sit amet, consectetuer adipiscing elit, sed diam nonummy nibh euismod tincidunt ut laoreet dolore magna aliquam erat</div>
  <div class="fav" style="top:443px;height:108px"><span class="num coral">36</span><span class="close"></span><h4>Lorem ipsum dolor sit amet, consectetuer adipiscing elit?</h4>Lorem ipsum dolor sit amet, consectetuer adipiscing elit, sed diam nonummy nibh euismod tincidunt ut</div>
</section>

<!-- 7 Tip categories -->
<section class="screen c1 r3">
  <header class="app-bar"><svg class="back" viewBox="0 0 12 18"><path d="M10 2L3 9l7 7" stroke="#fff" stroke-width="2.2" fill="none" stroke-linecap="round"/></svg><div class="brand">Lantern Quokka</div></header>
  <div class="title-bar"><span class="badge amber"><svg viewBox="0 0 16 16"><path d="M8 1.5a4.5 4.5 0 0 0-2.6 8.2V12h5.2V9.7A4.5 4.5 0 0 0 8 1.5z" fill="#fff"/><rect x="5.8" y="12.8" width="4.4" height="1.6" rx=".8" fill="#fff"/></svg></span>Interview Tips</div>
  <p class="prompt" style="top:167px">Select your Interview tip category</p>
  <div class="cat-btn" style="top:227px">Tips for before the interview</div>
  <div class="cat-btn" style="top:303px">Tips for during the interview</div>
  <div class="cat-btn" style="top:378px">Tips for after the interview</div>
  <div class="see-all" style="top:461px">See all</div>
</section>

<!-- 8 Tip list -->
<section class="screen c2 r3">
  <header class="app-bar"><svg class="back" viewBox="0 0 12 18"><path d="M10 2L3 9l7 7" stroke="#fff" stroke-width="2.2" fill="none" stroke-linecap="round"/></svg><div class="brand">Lantern Quokka</div></header>
  <div class="title-bar"><span class="badge amber"><svg viewBox="0 0 16 16"><path d="M8 1.5a4.5 4.5 0 0 0-2.6 8.2V12h5.2V9.7A4.5 4.5 0 0 0 8 1.5z" fill="#fff"/><rect x="5.8" y="12.8" width="4.4" height="1.6" rx=".8" fill="#fff"/></svg></span>Interview Tips</div>
  <div class="tip" style="top:147px"><span class="num amber">1</span>Start by researching the company an your interviewers</div>
  <div class="tip" style="top:213px"><span class="num amber">2</span>Practice your answers to common interview questions</div>
  <div class="tip" style="top:279px"><span class="num amber">3</span>Re-read the job description</div>
  <div class="tip" style="top:345px"><span class="num amber">4</span>Use th STAR method in answering questions</div>
  <div class="tip" style="top:411px"><span class="num amber">5</span>Recruit a friend to practice answering questions</div>
  <div class="tip" style="top:477px"><span class="num amber">6</span>Prepare a list of references</div>
  <div class="tip" style="top:543px"><span class="num amber">7</span>Be prepered with examples of your work</div>
</section>

<!-- 9 Tip detail with ad -->
<section class="screen c3 r3">
  <header class="app-bar"><svg class="back" viewBox="0 0 12 18"><path d="M10 2L3 9l7 7" stroke="#fff" stroke-width="2.2" fill="none" stroke-linecap="round"/></svg><div class="brand">Lantern Quokka</div></header>
  <div class="title-bar"><span class="badge amber"><svg viewBox="0 0 16 16"><path d="M8 1.5a4.5 4.5 0 0 0-2.6 8.2V12h5.2V9.7A4.5 4.5 0 0 0 8 1.5z" fill="#fff"/><rect x="5.8" y="12.8" width="4.4" height="1.6" rx=".8" fill="#fff"/></svg></span>Interview Tips</div>
  <div class="band amber" style="height:110px"></div>
  <div class="carousel-edge" style="left:0;top:147px;height:50px"></div>
  <div class="carousel-edge" style="right:0;top:147px;height:50px"></div>
  <div class="tip" style="top:147px"><span class="num amber">1</span>Start by researching the company an your interviewers</div>
  <div class="dots" style="top:216px"><i></i><i></i><i></i><i></i><i></i><i></i><i></i><i></i></div>
  <div class="abs" style="left:13px;top:260px;width:264px;height:158px;background:#fff;border-radius:5px;box-shadow:0 3px 8px rgba(0,0,0,.06);padding:11px 16px;font-size:11px;line-height:1.35;color:var(--muted)">Lorem ipsum dolor sit amet, consectetuer adipiscing elit, sed diam nonummy nibh euismod tincidunt ut laoreet dolore magna aliquam erat volutpat.<br>Ut wisi enim ad minim veniam, quis nostrud exerci tation ullamcorper suscipit lobortis nisl ut aliquip ex ea commodo consequat. Duis autem vel eum iriure dolor in hendrerit in vulputate velit esse molestie</div>
  <div class="abs" role="img" aria-label="Banner advertisement for a mobile game" style="left:0;bottom:0;width:290px;height:47px;background:linear-gradient(90deg,#2a5d8a 0%,#d08a3a 45%,#5a3a2a 75%,#f0a020 100%)"></div>
</section>

</body>
</html>
```